An Agro-Processor Needs a Packaging Design

We need packaging designs for a range of dried fruits and jams with a family look. The line-up has five variants of dried fruits and five variants of jams (the designs to include front and back of the packaging). The entire range will be marketed under the 'Petalvyn' brand name - please find the logo attached (the logo has a lock-up with the tagline). The packaging format for the dried fruits are resealable stand-up pouches and the jams are glass bottles - please find attached pictures of the packaging formats for reference.

Please find inspiration boards for the packaging design. Also find attached inspiration board for the design style required for the back of the dried fruit packaging.

For the dried fruit packaging, we need to develop a seal that conveys organic and sugar-free claims (please find attached example of a seal)

Target Market(s)

Organic and natural living enthusiasts who would pay a premium to get the best for them and their families

Industry/Entity Type

Food Production

Font styles to use
Sans Serif
Script

Colors

Designer to choose colors to be used in the design.

Requirements
Must have
• - The brand name 'petalvyn' is inspired by the abundance of nature in Africa, it also connotes organic, natural, freshness, delicateness, airiness, sophistication and premium and therefore the design should project these values
• - The design styling to be fun, modern and 'simplistic'
• - Please find below the packaging copy for both dried fruits and jams
• DRIED FRUIT FRONT PACKAGING:
• LOGO: Petalvyn - Sharing Earth's Warmth
• FIVE VARIANT NAMES: Plucky Pineapple | Dreamy Mango | Jolly Banana | Dapper Papaya | Breezy Jackfruit
• Dried
• DEVELOP A SEAL: 100% Organic | No Added Sugar (please see example attached)
• Ugandan Origin
• Net Weight: 100g
• DRIED FRUIT BACK COPY:
• Nature's best tasting fruits are also the healthiest which is why we have made it our mission to spread nature's love! Nourished by the tropical rains on the sun-drenched soils of Africa and cultivated by the caring hands of the local farmers, our organic range of dried fruits are nutrient-dense, high in fiber and rich in minerals. Enjoy them in your salads and cereals or simply relish them as a snack! They are diet-friendly if eaten in moderation and are a natural source of energy.
• VISUAL: Stack of Fruit Visual with arrows, each with the following claims (see examples attached in the inspiration boards):
• - 100% Organic
• - No Added Sugar
• - Nutrient-Dense
• - High in Fiber
• - Rich in Minerals
• INCLUDE: Nutritional Facts Table
• Ingredients: Mango - contains 100% fruit with no added sugars, preservatives, additives, colorings or flavorings.
• Reseal the pack to maintain freshness. Store in a cool and dry place.
• INCLUDE SPACE FOR: Batch Code / Expiry Date
• Barcode
• Produced by: Temari Food Industries, P. O. Box XXXXX, Kampala - Uganda.
• Find out more about us:
• Telephone: +XXX-XXX-XXXXXX
• Email: Info@TemariFoodIndustriez.com
• www.Chatterbook.net/Petalvyn
• JAM FRONT COPY:
• FIVE VARIANT NAMES: Plucky Pineapple with a Hint of Ginger | Dreamy Mango with a Kiss of Vanilla | Jolly Banana with a Twist of Chocolate | Dapper Papaya with a Pinch of Cardamon | Breezy Jackfruit with a Touch of Cinnamon
• Jam
• Ugandan Origin
• Net Weight: 400g
• JAM BACK COPY:
• Nature's best tasting fruits are also the healthiest which is why we have made it our mission to spread nature's love! Our range of jams come from fruits that have been nourished by the tropical rains on the sun-drenched soils of Africa and have been cultivated by the caring hands of the local farmers. We pride ourselves on making sure that the jams taste as delicious and look as natural as the perfectly ripened fruit! We then make it even better by pairing it with a hint of spice! Enjoy them in your breakfast or use them as a filling in baking.
• Ingredients: Mango, citric acid, sugar, pectin, vanilla
• Barcode
• Find out more about us:

```html
<!DOCTYPE html>
<html lang="en">
<head>
<meta charset="utf-8">
<title>Petalvyn – Plucky Pineapple Dried Fruit Label</title>
<link rel="stylesheet" href="https://fonts.googleapis.com/css2?family=Questrial&family=Dancing+Script:wght@500&family=Kalam:wght@400&family=Libre+Baskerville&display=swap">
<style>
  :root {
    --stage: #3db54b;
    --label-cream: #fbf3e0;
    --pattern-yellow: #f2cf1d;
    --pattern-green: #3aa447;
    --pattern-brown: #4a2a1a;
    --panel-cream: #f6edbd;
    --panel-edge: #fff8dc;
    --brand-brown: #4a2c20;
    --tagline-pink: #d9455f;
    --fruit-green: #8cbf3f;
    --pill-green: #2f6b2a;
    --gold-light: #f3d36b;
    --gold-dark: #b8891c;
  }
  * { margin: 0; padding: 0; box-sizing: border-box; }
  html, body { width: 1200px; height: 942px; overflow: hidden; }
  body { background: var(--stage); }
  .canvas { position: relative; width: 1200px; height: 942px; }
  .label { position: absolute; left: 284px; top: 31px; width: 632px; height: 880px; }
  .label svg { display: block; }
  .brand-name { font-family: "Questrial", sans-serif; font-size: 60px; fill: var(--brand-brown); }
  .brand-tagline { font-family: "Kalam", cursive; font-size: 17px; fill: var(--tagline-pink); }
  .variant-name { font-family: "Dancing Script", cursive; fill: var(--fruit-green); }
  .pill-text { font-family: "Questrial", sans-serif; font-size: 17px; fill: var(--pill-green); }
  .seal-text { font-family: "Libre Baskerville", serif; fill: var(--brand-brown); }
  .seal-ring-text { font-family: "Questrial", sans-serif; font-size: 12px; letter-spacing: 1px; fill: var(--brand-brown); }
  .origin-text { font-family: "Questrial", sans-serif; font-size: 17px; fill: var(--pill-green); }
</style>
</head>
<body>
<main class="canvas">
  <section class="label">
    <svg width="632" height="880" viewBox="0 0 632 880" xmlns="http://www.w3.org/2000/svg">
      <defs>
        <linearGradient id="pattern-tone" x1="0" y1="0" x2="1" y2="1">
          <stop offset="0" stop-color="var(--pattern-yellow)"/>
          <stop offset="0.35" stop-color="#c9a61e"/>
          <stop offset="0.55" stop-color="var(--pattern-green)"/>
          <stop offset="0.8" stop-color="#b7941c"/>
          <stop offset="1" stop-color="var(--pattern-yellow)"/>
        </linearGradient>
        <radialGradient id="gold-seal" cx="0.4" cy="0.35" r="0.7">
          <stop offset="0" stop-color="var(--gold-light)"/>
          <stop offset="1" stop-color="var(--gold-dark)"/>
        </radialGradient>
        <path id="organic-ring" d="M314,711 m-50,0 a50,50 0 1,1 100,0 a50,50 0 1,1 -100,0"/>
      </defs>

      <!-- label sheet -->
      <rect class="label-sheet" x="0" y="0" width="632" height="880" fill="var(--label-cream)"/>

      <!-- decorative pattern field -->
      <rect class="pattern-field" x="27" y="27" width="578" height="826" fill="url(#pattern-tone)"
            role="img" aria-label="African mandala-style pattern in yellow, green and brown"/>

      <!-- net weight seal -->
      <g class="net-weight-seal">
        <circle cx="314" cy="147" r="54" fill="var(--panel-cream)" opacity="0.8"/>
        <circle cx="314" cy="147" r="44" fill="url(#gold-seal)"/>
        <text class="seal-text" x="314" y="134" font-size="12" text-anchor="middle">NET</text>
        <text class="seal-text" x="314" y="149" font-size="12" text-anchor="middle">WEIGHT</text>
        <text class="seal-text" x="314" y="168" font-size="17" text-anchor="middle">100g</text>
      </g>

      <!-- central cartouche -->
      <path class="cartouche" d="M143,250 H489 A30,30 0 0 0 519,280 V584 A30,30 0 0 0 489,614 H143 A30,30 0 0 0 113,584 V280 A30,30 0 0 0 143,250 Z"
            fill="var(--panel-cream)" fill-opacity="0.93" stroke="var(--panel-edge)" stroke-width="8"/>
      <path class="cartouche-inner-line" d="M149,262 H483 A24,24 0 0 0 507,286 V578 A24,24 0 0 0 483,602 H149 A24,24 0 0 0 125,578 V286 A24,24 0 0 0 149,262 Z"
            fill="none" stroke="#e6d894" stroke-width="1.5"/>

      <text class="brand-name" x="316" y="352" text-anchor="middle">petalvyn</text>
      <text class="brand-tagline" x="316" y="383" text-anchor="middle">Sharing Earth's Warmth</text>

      <text class="variant-name" x="316" y="426" font-size="34" text-anchor="middle">Plucky</text>
      <text class="variant-name" x="316" y="474" font-size="52" text-anchor="middle">Pineapple</text>

      <g class="product-type-pill">
        <rect x="252" y="525" width="128" height="36" rx="10" fill="none" stroke="var(--pill-green)" stroke-width="2"/>
        <text class="pill-text" x="316" y="549" text-anchor="middle">Dried Fruit</text>
      </g>

      <!-- organic claim seal -->
      <g class="organic-seal">
        <circle cx="314" cy="711" r="72" fill="var(--panel-cream)" opacity="0.8"/>
        <circle cx="314" cy="711" r="64" fill="url(#gold-seal)"/>
        <circle cx="314" cy="711" r="38" fill="none" stroke="var(--brand-brown)" stroke-width="1.5"/>
        <text class="seal-ring-text">
          <textPath href="#organic-ring" startOffset="0">100% ORGANIC • NO ADDED SUGAR •</textPath>
        </text>
      </g>

      <!-- origin tab -->
      <g class="origin-tab">
        <path d="M210,853 V828 Q210,816 222,816 H410 Q422,816 422,828 V853 Z" fill="var(--panel-cream)"/>
        <circle cx="232" cy="835" r="3.5" fill="var(--pattern-green)"/>
        <circle cx="400" cy="835" r="3.5" fill="var(--pattern-green)"/>
        <text class="origin-text" x="316" y="841" text-anchor="middle">Ugandan Origin</text>
      </g>
    </svg>
  </section>
</main>
</body>
</html>
```